Nurturing Victors 6x9 book soft cover- front cover only

We need a book cover for a softcover book. We will need final files in Photoshop or InDesign is preferred.

Overall Title:
Nurturing Victors
Subtitle:
The Foundations of Humble Mentoring for Trainers, Instructors and Players
Author:
by Dr. Martin Hollis

The audience is high school and college coaches however we don't want the standard picture with words over the top. Make it a creative design but keep it mind it's a little academic.

```html
<!DOCTYPE html>
<html lang="en">
<head>
<meta charset="UTF-8">
<title>Nurturing Victors – Front Cover</title>
<link href="https://fonts.googleapis.com/css2?family=Antonio:wght@400;700&family=Oswald:wght@500&display=swap" rel="stylesheet">
<style>
  :root {
    --backdrop: #4b4b4b;
    --paper: #ffffff;
    --navy: #1f3c74;
    --gold-dark: #a97a0c;
    --gold-light: #e3b935;
    --ink: #1a1a1a;
    --curl-shadow: #bdbdbd;
    --sky: #3f7fd0;
    --dusk: #f0c27a;
    --rock: #5a2e1e;
  }
  * { margin: 0; padding: 0; box-sizing: border-box; }
  html, body {
    width: 1200px; height: 1200px; overflow: hidden;
    background: var(--backdrop);
  }
  .cover {
    position: absolute;
    left: 230px; top: 45px;
    width: 740px; height: 1110px;
    background: var(--paper);
    overflow: hidden;
  }
  .title {
    position: absolute;
    left: 50px; top: 100px;
    width: 640px;
    font-family: "Antonio", "Arial Narrow", sans-serif;
    font-weight: 700;
    font-size: 210px;
    line-height: 0.98;
    letter-spacing: -2px;
    white-space: nowrap;
  }
  .title-line {
    display: block;
    width: max-content;
    transform: scaleX(0.8);
    transform-origin: left center;
  }
  .title-first { color: var(--navy); }
  .title-second {
    background: linear-gradient(90deg, var(--gold-dark) 0%, var(--gold-light) 50%, var(--gold-dark) 100%);
    -webkit-background-clip: text;
    background-clip: text;
    color: transparent;
  }
  .subtitle {
    position: absolute;
    left: 70px; top: 600px;
    width: 560px;
    font-family: "Antonio", "Arial Narrow", sans-serif;
    font-weight: 400;
    font-size: 44px;
    line-height: 1.6;
    color: var(--ink);
  }
  .subtitle-lead { color: var(--gold-dark); }
  .author {
    position: absolute;
    left: 70px; top: 960px;
    font-family: "Oswald", "Arial Narrow", sans-serif;
    font-weight: 500;
    font-size: 34px;
    letter-spacing: 6px;
    color: var(--ink);
    text-transform: uppercase;
    white-space: nowrap;
  }
  .page-curl {
    position: absolute;
    left: 0; top: 0;
    width: 740px; height: 1110px;
  }
</style>
</head>
<body>
  <main class="cover">
    <svg class="page-curl" viewBox="0 0 740 1110" xmlns="http://www.w3.org/2000/svg">
      <defs>
        <linearGradient id="revealGradient" x1="1" y1="0" x2="0.3" y2="1">
          <stop offset="0" stop-color="#3f7fd0"/>
          <stop offset="0.45" stop-color="#f0c27a"/>
          <stop offset="1" stop-color="#5a2e1e"/>
        </linearGradient>
        <linearGradient id="flapGradient" x1="0" y1="0" x2="1" y2="0">
          <stop offset="0" stop-color="#ffffff"/>
          <stop offset="0.6" stop-color="#e6e6e6"/>
          <stop offset="1" stop-color="#bdbdbd"/>
        </linearGradient>
      </defs>
      <path role="img" aria-label="Photo of three climbers cheering on a mountain summit at sunrise"
            d="M740,600 L740,1110 L330,1110 C470,1010 640,760 740,600 Z"
            fill="url(#revealGradient)"/>
      <path class="curl-flap"
            d="M740,600 C640,760 470,1010 330,1110 C420,990 470,870 500,800 C530,730 600,690 740,600 Z"
            fill="url(#flapGradient)"/>
    </svg>

    <h1 class="title">
      <span class="title-line title-first">Nurturing</span>
      <span class="title-line title-second">Victors</span>
    </h1>

    <p class="subtitle">
      <span class="subtitle-lead">The Foundations</span> of Humble Mentoring
      for Trainers, Instructors and Players
    </p>

    <p class="author">Dr. Martin Hollis</p>
  </main>
</body>
</html>
```